Business Cards for a small business advisory (business services)

Professional look. Same as would apply for a lawyer, accountant, or other financial services professional. Please use the logo colors

Target Market(s)

small business owners

Industry/Entity Type

Financial Servics

Contact Information for Business Card

Name: Gavin L. Whitmore, CAIA / Title: Business Advisor / Office #: (718) 294-7716 / Mobile #: (917) 382-5047 / Email: g.whitmore@clearfieldventurepartners.example / Web: www.clearfieldventurepartners.example

Font styles to use
Sans Serif

```html
<!DOCTYPE html>
<html lang="en">
<head>
<meta charset="utf-8">
<title>Clearfield Venture Partners – Business Cards</title>
<link rel="stylesheet" href="https://fonts.googleapis.com/css2?family=Montserrat:wght@700&family=Poppins:wght@400;500;600&display=swap">
<style>
  :root {
    --navy: #1d3461;
    --green: #7dc242;
    --paper: #ffffff;
    --backdrop: #f1f2f4;
    --ink: #1f2a44;
    --rule: #1d3461;
  }
  * { box-sizing: border-box; margin: 0; padding: 0; }
  html, body { width: 1200px; height: 1200px; overflow: hidden; }
  body {
    background: var(--backdrop);
    display: flex;
    align-items: center;
    justify-content: center;
    gap: 60px;
    font-family: "Poppins", sans-serif;
    color: var(--ink);
  }
  .card {
    position: relative;
    width: 540px;
    height: 310px;
    background: var(--paper);
    box-shadow: 10px 14px 22px rgba(0, 0, 0, 0.28);
    overflow: hidden;
  }

  /* Brand lockup */
  .brand { display: flex; align-items: center; gap: 10px; }
  .brand-dot {
    width: 34px; height: 34px; border-radius: 50%;
    background: var(--navy); flex: none;
  }
  .brand-name {
    font-family: "Montserrat", sans-serif;
    font-weight: 700;
    color: var(--navy);
    line-height: 1.05;
  }

  /* Front */
  .card-front .brand {
    position: absolute; left: 0; right: 0; top: 118px;
    justify-content: center;
  }
  .card-front .brand-name { font-size: 30px; }
  .card-front .web-row {
    position: absolute; left: 0; right: 0; top: 244px;
    display: flex; align-items: center; gap: 18px;
  }
  .web-row .rule { flex: 1; height: 1.5px; background: var(--rule); }
  .web-row .web {
    font-size: 12px; letter-spacing: 2.2px; color: var(--ink); white-space: nowrap;
  }

  /* Back */
  .card-back .brand { position: absolute; left: 30px; top: 44px; }
  .card-back .brand-dot { width: 28px; height: 28px; }
  .card-back .brand-name { font-size: 24px; }
  .name-band {
    position: absolute; right: 0; top: 142px;
    width: 290px; height: 30px;
    background: var(--navy);
    color: #fff;
    font-weight: 600;
    font-size: 16px;
    letter-spacing: 0.5px;
    line-height: 30px;
    padding-left: 12px;
    white-space: nowrap;
  }
  .job-title {
    position: absolute; left: 262px; top: 178px;
    font-size: 13px; letter-spacing: 1px; color: var(--ink);
  }
  .contact {
    position: absolute; display: flex; align-items: center; gap: 12px;
    font-size: 13px; font-weight: 500; color: var(--navy); white-space: nowrap;
  }
  .contact .icon {
    width: 17px; height: 17px; border-radius: 50%;
    background: var(--green); flex: none;
    display: flex; align-items: center; justify-content: center;
  }
  .contact .icon svg { width: 10px; height: 10px; }
  .contact-office { left: 198px; top: 233px; }
  .contact-mobile { left: 366px; top: 233px; }
  .contact-email { left: 198px; top: 268px; font-size: 12px; }
  .footer-bar {
    position: absolute; left: 78px; right: 0; bottom: 0;
    height: 8px; background: var(--green);
  }
</style>
</head>
<body>

  <section class="card card-front" aria-label="Business card front">
    <div class="brand">
      <span class="brand-dot"></span>
      <span class="brand-name">Clearfield Venture Partners</span>
    </div>
    <div class="web-row">
      <span class="rule"></span>
      <span class="web">www.clearfieldventurepartners.example</span>
      <span class="rule"></span>
    </div>
  </section>

  <section class="card card-back" aria-label="Business card back">
    <div class="brand">
      <span class="brand-dot"></span>
      <span class="brand-name">Clearfield Venture Partners</span>
    </div>

    <div class="name-band">GAVIN L. WHITMORE, CAIA</div>
    <div class="job-title">BUSINESS ADVISOR</div>

    <div class="contact contact-office">
      <span class="icon">
        <svg viewBox="0 0 10 10"><path d="M2.2 1 L3.6 1 L4.2 3 L3.3 3.8 Q4.2 5.8 6.2 6.7 L7 5.8 L9 6.4 L9 7.8 Q8.6 9 7.4 9 Q1 8.2 1 2.6 Q1 1.4 2.2 1 Z" fill="#fff"/></svg>
      </span>
      (718) 294-7716
    </div>

    <div class="contact contact-mobile">
      <span class="icon">
        <svg viewBox="0 0 10 10"><rect x="2.5" y="0.8" width="5" height="8.4" rx="1" fill="#fff"/><rect x="3.4" y="1.8" width="3.2" height="5.4" fill="#7dc242"/></svg>
      </span>
      (917) 382-5047
    </div>

    <div class="contact contact-email">
      <span class="icon">
        <svg viewBox="0 0 10 10"><rect x="1" y="2.2" width="8" height="5.6" fill="#fff"/><path d="M1 2.4 L5 5.4 L9 2.4" fill="none" stroke="#7dc242" stroke-width="0.9"/></svg>
      </span>
      g.whitmore@clearfieldventurepartners.example
    </div>

    <div class="footer-bar"></div>
  </section>

</body>
</html>
```